Taomeng business card -we import and distributed Chinese herbal medicine into Australia for prac...

We need a business card for our recently purchased and rebranded company. We are a small family run business - husband and wife team. Our logo is red and black, and we would like the card to be white, with an element of gold in the design (the first cloud in the attached png) which when printed we would like embossed in gold. Our website uses Chinese water colour paintings in the banners (www.taomeng.net.au) so a design that is in harmony with this would be ideal.
side one needs to include:

Target Market(s)

potential customers

Industry/Entity Type

Health And Wellness

Contact Information for Business Card

Side 1
logo,
Edmund Varsk Director
Practitioner Support and Education
0491 722 413
edmund@taomeng.net.au
218 Colbury St, Karrowby, TAS, 7352

side 2 needs to include:
logo
Priscilla Moult Director
Orders, Accounts and Despatch
0487 530 619
priscilla@taomeng.net.au

Font styles to use
Serif

Colors

Designer to choose colors to be used in the design.

Requirements
Must have
• black, red, gold colours
Nice to have
• we like the font papyrus (mac font)

```html
<!DOCTYPE html>
<html lang="en">
<head>
<meta charset="utf-8">
<title>Taomeng business cards</title>
<link href="https://fonts.googleapis.com/css2?family=Montserrat:wght@400;500;700&display=swap" rel="stylesheet">
<style>
  :root {
    --backdrop: #3b3c3f;
    --card-white: #f4f6f9;
    --card-black: #232324;
    --ink-navy: #1d2742;
    --name-blue: #1f5c9e;
    --seal-red: #d62b20;
    --gold-light: #f6d774;
    --gold-deep: #c9962b;
    --wash-pale: #dbe4ef;
    --wash-mid: #8fa8cb;
    --wash-deep: #3d5f95;
    --text-dark: #1a1a1a;
    --text-light: #f2f2f2;
  }
  * { box-sizing: border-box; margin: 0; padding: 0; }
  html, body { width: 1200px; height: 1021px; overflow: hidden; }
  body {
    background: var(--backdrop);
    font-family: "Montserrat", sans-serif;
    position: relative;
  }
  .card {
    position: absolute;
    left: 220px;
    width: 760px;
    height: 465px;
    overflow: hidden;
    box-shadow: 0 10px 30px rgba(0,0,0,.35);
  }
  .card--front { top: 30px; background: var(--card-white); color: var(--text-dark); }
  .card--back { top: 526px; background: var(--card-black); color: var(--text-light); }

  .emboss-cloud {
    position: absolute; left: 110px; top: 36px; width: 130px; height: 52px;
    border-radius: 50%;
    background: radial-gradient(ellipse at center, #e3e7ed 0%, rgba(227,231,237,0) 72%);
  }
  .wash-landscape {
    position: absolute; left: 0; right: 0; bottom: 0; height: 200px;
    background: linear-gradient(180deg, rgba(219,228,239,0) 0%, var(--wash-pale) 35%, var(--wash-mid) 70%, var(--wash-deep) 100%);
  }
  .wash-moon {
    position: absolute; left: 505px; top: 62px; width: 215px; height: 210px;
    border-radius: 50%;
    background: radial-gradient(circle at 50% 45%, #5a77a6 0%, #2f4776 65%, rgba(47,71,118,.2) 100%);
  }

  .person { position: absolute; }
  .person__name { font-weight: 700; color: var(--name-blue); }
  .person__role { font-weight: 400; }

  .card--front .person { left: 92px; top: 138px; font-size: 17px; line-height: 22px; }
  .card--front .person__name { font-size: 22px; line-height: 28px; }

  .contacts { position: absolute; list-style: none; font-size: 17px; line-height: 25px; }
  .contacts li { display: flex; align-items: center; gap: 8px; }
  .contacts svg { width: 14px; height: 14px; flex: none; }
  .card--front .contacts { left: 92px; top: 222px; }

  .brand { position: absolute; display: flex; align-items: center; gap: 14px; }
  .brand__mark { width: 36px; height: 56px; background: var(--seal-red); }
  .brand__name { font-weight: 500; letter-spacing: 2px; white-space: nowrap; }
  .card--front .brand { left: 455px; top: 345px; }
  .card--front .brand__name { font-size: 42px; color: var(--ink-navy); }

  .card--back .brand { left: 55px; top: 45px; }
  .card--back .brand__name { font-size: 46px; color: var(--text-light); }

  .gold-cloud {
    position: absolute; left: 565px; top: 190px; width: 150px; height: 62px;
    border-radius: 48% 52% 40% 45%;
    background: linear-gradient(160deg, var(--gold-light) 0%, var(--gold-deep) 100%);
  }
  .card--back .person { right: 60px; top: 268px; text-align: right; font-size: 18px; line-height: 23px; }
  .card--back .person__name { font-size: 25px; line-height: 30px; }
  .card--back .contacts { left: 60px; top: 265px; }
  .address { position: absolute; left: 60px; top: 350px; font-size: 17px; }
</style>
</head>
<body>
  <section class="card card--front">
    <div class="emboss-cloud" role="img" aria-label="Blind-embossed auspicious cloud ornament"></div>
    <div class="wash-landscape" role="img" aria-label="Chinese watercolour painting of misty blue mountains"></div>
    <div class="wash-moon" role="img" aria-label="Watercolour ink moon with cranes in flight"></div>

    <div class="person">
      <p class="person__name">Priscilla Moult</p>
      <p class="person__role">Director</p>
      <p class="person__role">Orders, Accounts and Despatch</p>
    </div>

    <ul class="contacts">
      <li><svg viewBox="0 0 16 16"><path fill="#d62b20" d="M3.5 1l2.5 3-1.5 1.8c.9 2 2.6 3.7 4.7 4.7L11 9l3 2.5-1.3 2.7C7 14 2 9 1.8 3.3z"/></svg>0487 530 619</li>
      <li><svg viewBox="0 0 16 16"><rect x="1" y="3" width="14" height="10" fill="none" stroke="#d62b20" stroke-width="1.6"/><path d="M1 3l7 6 7-6" fill="none" stroke="#d62b20" stroke-width="1.6"/></svg>priscilla@taomeng.net.au</li>
      <li><svg viewBox="0 0 16 16"><circle cx="8" cy="8" r="6.5" fill="none" stroke="#d62b20" stroke-width="1.5"/><path d="M1.5 8h13M8 1.5c-3 3.5-3 9.5 0 13M8 1.5c3 3.5 3 9.5 0 13" fill="none" stroke="#d62b20" stroke-width="1.2"/></svg>www.taomeng.net.au</li>
    </ul>

    <div class="brand">
      <span class="brand__mark"></span>
      <span class="brand__name">Taomeng</span>
    </div>
  </section>

  <section class="card card--back">
    <div class="brand">
      <span class="brand__mark"></span>
      <span class="brand__name">Taomeng</span>
    </div>

    <div class="gold-cloud" role="img" aria-label="Gold foil embossed auspicious cloud ornament"></div>

    <div class="person">
      <p class="person__name">Edmund Varsk</p>
      <p class="person__role">Director</p>
      <p class="person__role">Practitioner Support and Education</p>
    </div>

    <ul class="contacts">
      <li><svg viewBox="0 0 16 16"><path fill="#d62b20" d="M3.5 1l2.5 3-1.5 1.8c.9 2 2.6 3.7 4.7 4.7L11 9l3 2.5-1.3 2.7C7 14 2 9 1.8 3.3z"/></svg>0491 722 413</li>
      <li><svg viewBox="0 0 16 16"><rect x="1" y="3" width="14" height="10" fill="none" stroke="#d62b20" stroke-width="1.6"/><path d="M1 3l7 6 7-6" fill="none" stroke="#d62b20" stroke-width="1.6"/></svg>edmund@taomeng.net.au</li>
      <li><svg viewBox="0 0 16 16"><circle cx="8" cy="8" r="6.5" fill="none" stroke="#d62b20" stroke-width="1.5"/><path d="M1.5 8h13M8 1.5c-3 3.5-3 9.5 0 13M8 1.5c3 3.5 3 9.5 0 13" fill="none" stroke="#d62b20" stroke-width="1.2"/></svg>www.taomeng.net.au</li>
    </ul>
    <p class="address">218 Colbury St, Karrowby, TAS, 7352</p>
  </section>
</body>
</html>
```